we are an outdoor outlet in a country club that has a variety of outlets. The Club is called Brindlewood and is located in Cairo, Egypt. This garden menu will include cuisines from the Mediterranean, Asia and Texmex. we need a menu that is colorful and would fit an A3 size, back and front are to be used. Attached is the old menu currently in use (Garden Menu 2012.pdf is just for reference) and the new menu text for you to use is under the name Garden Menu Fall 2013
thank you.

```html
<!DOCTYPE html>
<html lang="en">
<head>
<meta charset="utf-8">
<title>Brindlewood Country Club – Garden Menu</title>
<link href="https://fonts.googleapis.com/css2?family=Quicksand:wght@500&family=Archivo:wght@800&family=Roboto+Condensed:wght@400&display=swap" rel="stylesheet">
<style>
  :root {
    --backdrop: #7b7b7b;
    --frame: #000000;
    --header: #ffffff;
    --sand: #e4d27f;
    --sand-light: #ecdc95;
    --sand-dark: #d9c46a;
    --leaf: #b9cc1e;
    --ink: #3d2414;
    --band: #ffffff;
  }
  * { margin: 0; padding: 0; box-sizing: border-box; }
  html, body { width: 1200px; height: 800px; overflow: hidden; }
  body {
    background: var(--backdrop);
    position: relative;
    font-family: "Roboto Condensed", "Arial Narrow", sans-serif;
    color: var(--ink);
  }
  .menu-page {
    position: absolute;
    top: 88px;
    width: 452px;
    height: 638px;
    border: 5px solid var(--frame);
    background: var(--sand);
    overflow: hidden;
  }
  .menu-page--front { left: 110px; }
  .menu-page--back { left: 638px; }

  .page-texture {
    position: absolute;
    left: 0; right: 0; top: 118px; bottom: 0;
    background: linear-gradient(160deg, var(--sand-light) 0%, var(--sand) 45%, var(--sand-dark) 100%);
  }
  .page-header {
    position: absolute;
    left: 0; top: 0; right: 0; height: 118px;
    background: var(--header);
  }
  .menu-tab {
    position: absolute;
    left: 3px; top: 0;
    width: 34px; height: 112px;
    background: var(--frame);
    color: #fff;
    font-family: "Archivo", sans-serif;
    font-weight: 800;
    font-size: 17px;
    letter-spacing: 1px;
    writing-mode: vertical-rl;
    display: flex; align-items: center; justify-content: flex-start;
    padding-top: 10px;
  }
  .brand {
    position: absolute;
    left: 0; right: 0; top: 32px;
    display: flex; align-items: center; justify-content: center; gap: 10px;
  }
  .brand-dot {
    width: 34px; height: 34px; border-radius: 50%;
    background: var(--leaf);
  }
  .brand-name {
    font-family: "Quicksand", sans-serif;
    font-weight: 500;
    font-size: 26px;
    line-height: 1;
    color: var(--ink);
  }
  .cuisine-tag {
    position: absolute;
    transform: translateX(-50%);
    background: var(--leaf);
    color: #fff;
    font-family: "Archivo", sans-serif;
    font-weight: 800;
    font-size: 10.5px;
    padding: 5px 12px;
    white-space: nowrap;
    clip-path: polygon(2% 0, 100% 6%, 98% 100%, 0 94%);
  }
  .white-band {
    position: absolute;
    left: 0; right: 0;
    background: var(--band);
  }
  .menu-section {
    position: absolute;
    transform: translateX(-50%);
    text-align: center;
    white-space: nowrap;
  }
  .section-title {
    font-family: "Archivo", sans-serif;
    font-weight: 800;
    font-size: 9px;
    margin-bottom: 6px;
  }
  .dish {
    font-size: 5.2px;
    line-height: 6.3px;
  }
</style>
</head>
<body>

<section class="menu-page menu-page--front">
  <div class="page-texture" role="img" aria-label="Soft diamond pattern background in sand tones"></div>
  <header class="page-header">
    <div class="menu-tab">MENU</div>
    <div class="brand"><span class="brand-dot"></span><span class="brand-name">brindlewood country club</span></div>
  </header>
  <div class="cuisine-tag" style="left:223px; top:117px;">Mediterranean Corner</div>

  <div class="menu-section" style="left:138px; top:180px;">
    <h3 class="section-title">Soups:</h3>
    <p class="dish">Tomato Basil</p>
    <p class="dish">Simmered tomato soup finished with fresh basil and cream</p>
    <p class="dish">Chicken Cream</p>
    <p class="dish">Chicken broth with roasted chicken cubes, pine nuts, and cream</p>
    <p class="dish">Moroccan Harira</p>
    <p class="dish">Vegetable broth with fresh tomato, chickpeas, lentil, cilantro, and diced lamb</p>
  </div>

  <div class="menu-section" style="left:138px; top:250px;">
    <h3 class="section-title">Salads:</h3>
    <p class="dish">Caprese</p>
    <p class="dish">Buffalo mozzarella and sliced tomato with a balsamic vinaigrette</p>
    <p class="dish">Rocket Apple</p>
    <p class="dish">Rocket leaves with gorgonzola, croutons, and strawberry vinaigrette</p>
    <p class="dish">French Riviera Nicoise</p>
    <p class="dish">Lettuce, egg, tomato, tuna, olives, onion, celery, radish, bell pepper in a French vinaigrette</p>
    <p class="dish">Folie</p>
    <p class="dish">Mixed greens with crab sticks, mushroom, corn, cherry tomato in a mango vinaigrette</p>
  </div>

  <div class="menu-section" style="left:138px; top:356px;">
    <h3 class="section-title">Sauces:</h3>
    <p class="dish">Napolitana, Bolognese, Alfredo</p>
  </div>

  <div class="menu-section" style="left:138px; top:402px;">
    <h3 class="section-title">Sandwiches:</h3>
    <p class="dish">(Served with French fries or a garden salad)</p>
    <p class="dish">Beef or chicken Shawerma</p>
    <p class="dish">Grilled kofta</p>
    <p class="dish">Greek lamb gyro in pita bread with Tzatziki</p>
    <p class="dish">Club sandwich with smoked beef, turkey, egg</p>
  </div>

  <div class="menu-section" style="left:337px; top:180px;">
    <h3 class="section-title">Appetizers:</h3>
    <p class="dish">Salmon tartare seasoned with lemon juice, garlic, and crushed black pepper</p>
    <p class="dish">Roasted eggplant rolls with herbed ricotta cheese and pine nuts</p>
    <p class="dish">Falafel in mini pita served with tehina and oriental salsa</p>
    <p class="dish">Manksusha with thyme and olive oil</p>
    <p class="dish">Fried kobeba with minced meat, spices, and pine nuts</p>
    <p class="dish">Fried calamari a la Romana served with aioli</p>
    <p class="dish">Sambousek with herbed white cheese and mint</p>
    <p class="dish">Oriental sausage sautéed with garlic and onion</p>
    <p class="dish">Mini vine leaves with a yoghurt dip</p>
    <p class="dish">Fatouch with a pomegranate syrup dressing</p>
    <p class="dish">Hummus seasoned with lemon juice, garlic, and olive oil</p>
    <p class="dish">White cheese with diced tomato, thyme, and olive oil</p>
    <p class="dish">Tehina seasoned with cumin, lemon juice, and garlic</p>
  </div>

  <div class="menu-section" style="left:337px; top:330px;">
    <h3 class="section-title">Pizza &amp; Pasta:</h3>
    <p class="dish">Pizza Margarita (Choose your toppings)</p>
    <p class="dish">Create your own pasta</p>
    <p class="dish">Type: Spaghetti, Tagliatelle, Penne</p>
  </div>

  <div class="menu-section" style="left:337px; top:397px;">
    <h3 class="section-title">Toppings:</h3>
    <p class="dish">Bell peppers, olives, tomato, onion</p>
    <p class="dish">Mushroom, chicken, tuna, pepperoni</p>
    <p class="dish">Smoked salmon, shrimps</p>
    <p class="dish">Lasagna</p>
  </div>

  <div class="menu-section" style="left:223px; top:492px;">
    <h3 class="section-title">Main Courses:</h3>
    <p class="dish">Veal Parmeggiana</p>
    <p class="dish">Breaded veal escalope topped with melted cheese and tomato sauce served with Spaghetti</p>
    <p class="dish">Chicken a la Francaise</p>
    <p class="dish">Pan fried chicken breast in a mushroom cream sauce with vegetables white rice</p>
    <p class="dish">Grilled Salmon</p>
    <p class="dish">Salmon steak charcoal grilled with avocado tomato relish and creamy mushroom risotto</p>
    <p class="dish">Moroccan Chicken</p>
    <p class="dish">Chicken cubes simmered with spices and olives served with tomato rice</p>
    <p class="dish">Filet</p>
    <p class="dish">Tender filet grilled to your liking served with mashed potato and creamed spinach</p>
    <p class="dish">Choice of sauces: Brown mushroom, Green Peppercorn, Gorgonzola</p>
  </div>
</section>

<section class="menu-page menu-page--back">
  <div class="page-texture" role="img" aria-label="Soft diamond pattern background in sand tones"></div>
  <header class="page-header">
    <div class="menu-tab">MENU</div>
    <div class="brand"><span class="brand-dot"></span><span class="brand-name">brindlewood country club</span></div>
  </header>
  <div class="cuisine-tag" style="left:227px; top:112px;">Asian Corner</div>

  <div class="menu-section" style="left:318px; top:142px;">
    <h3 class="section-title">Main Courses:</h3>
    <p class="dish">Murgh Chicken Makhni</p>
    <p class="dish">Chicken cubes in a rich creamy tomato sauce seasoned with garam masala</p>
  </div>

  <div class="menu-section" style="left:133px; top:170px;">
    <h3 class="section-title">Salads &amp; Appetizers:</h3>
    <p class="dish">Chicken Wasabi Salad</p>
    <p class="dish">Diced chicken with a mayo wasabi dressing on top of shredded lettuce</p>
    <p class="dish">Chicken Sesame Noodle Salad</p>
    <p class="dish">Sesame crusted chicken with glass noodles tossed with sweet chili, soy sauce, and lemongrass</p>
    <p class="dish">Spring rolls</p>
    <p class="dish">Vegetable spring rolls served with house made sweet and sour dip</p>
    <p class="dish">Indian Samosa</p>
    <p class="dish">Fried dough parcels filled with vegetables and spices</p>
  </div>

  <div class="menu-section" style="left:318px; top:217px;">
    <h3 class="section-title">Choice of side:</h3>
    <p class="dish">vegetable korma or curd</p>
    <p class="dish">Chicken Tandoori</p>
    <p class="dish">Grilled chicken cubes with tandoori spices served with basmati rice</p>
    <p class="dish">Thai Coconut Curry Shrimp</p>
    <p class="dish">Sautéed shrimp tossed with curry and coconut milk served with jasmine rice</p>
    <p class="dish">Mongolian Beef</p>
    <p class="dish">Soy marinated beef with oyster sauce and vegetables served with egg noodles</p>
  </div>

  <div class="white-band" style="top:290px; height:30px;"></div>
  <div class="cuisine-tag" style="left:227px; top:306px;">Tex Mex</div>

  <div class="menu-section" style="left:227px; top:350px;">
    <h3 class="section-title" style="margin-bottom:2px;">Salads &amp; Appetizers:</h3>
    <p class="dish">Caesar Salad</p>
    <p class="dish">Iceberg lettuce with Caesar dressing with grated Parmesan cheese and croutons</p>
    <p class="dish">Taco salad 42</p>
    <p class="dish">Chicken breast, beans, sour cream, guacamole, tomato, corn, lettuce, olives, chives, vinaigrette</p>
    <p class="dish">Nachos topped with chili, melted cheese, beans</p>
    <p class="dish">Chicken Quesadilla served with guacamole, salsa, and sour cream</p>
    <p class="dish">Main Courses &amp; Sandwiches:</p>
    <p class="dish">Cheeseburger</p>
    <p class="dish">House made lean beef burger topped with cheddar cheese</p>
    <p class="dish">Mushroom Burger</p>
    <p class="dish">Beef burger with sautéed mushroom, caramelized onion, and provolone cheese</p>
    <p class="dish">Crispy Chicken Wrap</p>
    <p class="dish">Crisp fried chicken wrap with a ranch dressing</p>
    <p class="dish">Fajita (Chicken, Beef, Combo)</p>
    <p class="dish">Pan seared meat or chicken with onion and bell pepper served with sour cream, guacamole, salsa</p>
  </div>

  <div class="white-band" style="top:472px; height:26px;"></div>
  <div class="cuisine-tag" style="left:227px; top:492px;">Desserts</div>

  <div class="menu-section" style="left:227px; top:522px;">
    <p class="dish">Mix Berries Cheesecake</p>
    <p class="dish">Crème Brulee</p>
    <p class="dish">Chocolate Caramel Cake</p>
    <p class="dish">Warm Chocolate Fondant</p>
    <p class="dish">Baked Apple Tart Tatin</p>
    <p class="dish">Tiramisu</p>
    <p class="dish">Pumpkin Pie Pan</p>
    <p class="dish">Mixed Berries Granola Yoghurt</p>
    <p class="dish">Vanilla Ice Cream Profiterole with dark and white chocolate sauce</p>
    <p class="dish">Caramelized Banana with Deep Fried Ice Cream</p>
    <p class="dish">Baklava with Nuts and Sugar Syrup</p>
    <p class="dish">Shot Glass Sampler – Tiramisu, Chocolate Crisp Mousse, Pear with Sabayon</p>
    <p class="dish">Ice Cream by Scoop</p>
  </div>
</section>

</body>
</html>
```